TALLIS AT DWELLINGS, LLC Webpage portfolio

I want to create a Website that allows my potential clients to browse my Skilled work via before and after photos. I want the website to enhance the work that I provide and potentially drive new business, or at least solidify my work.
I also do 3D CAD and Modeling of New Spaces and it would be nice to show some of that work from pencil design to 3D modeling, which I feel may help give me more clients.

The website needs to show a solid carpenter/company with the skills to get any project completed.

Types of Jobs - Custom Carpentry & Finishes, Kitchens, Baths, Basements, Decks, Porches, Whole House Renovation - Skilled Craftsmanship (Hardwood Flooring, Floor and Wall Tile) and much more...

Target Market(s)

Residential Home Renovation, Kitchen and Bath Renovation, Home Improvement

Industry/Entity Type

Residential Construction

Number of Pages Required

5+ page

Font styles to use
Sans Serif
Script

Requirements
Must have
• Similar to Rimvale.com, except for Tallis At Dwellings.
• Must be inviting.
• My Services Offered
• A way to reach me or contact me for estimates with some sort of Screening Questionare.
Nice to have
• Inviting Colors
Should not have
• Not sure at this time

```html
<!DOCTYPE html>
<html lang="en">
<head>
<meta charset="utf-8">
<title>Tallis At Dwellings — Client Feedback</title>
<link rel="stylesheet" href="https://fonts.googleapis.com/css2?family=Questrial&display=swap">
<style>
:root{
  --page-dark:#141312;
  --header-bg:#1c1a18;
  --nav-text:#6d6a66;
  --photo-a:#3a2a1c;
  --photo-b:#6a4a2c;
  --photo-c:#1e1814;
  --ghost-text:#cfd3d6;
  --modal-bg:rgba(238,241,243,0.9);
  --ink:#0c0c0c;
  --thumb:#f4f6f7;
}
*{margin:0;padding:0;box-sizing:border-box}
html,body{width:1200px;height:800px;overflow:hidden;background:var(--page-dark)}
body{font-family:'Questrial',sans-serif;position:relative}
.site-header{position:absolute;left:0;top:0;width:1200px;height:100px;background:var(--header-bg)}
.brand{position:absolute;left:30px;top:62px;display:flex;align-items:center;gap:6px;color:#5f5c58;font-size:13px}
.brand-mark{width:10px;height:10px;background:#5f5c58}
.social{position:absolute;left:294px;top:67px;display:flex;gap:12px}
.social span{width:12px;height:12px;border-radius:50%;background:#5f5c58}
.main-nav{position:absolute;right:28px;top:66px;display:flex;gap:31px;font-size:12px;letter-spacing:3px;color:var(--nav-text)}
.hero-photo{position:absolute;left:0;top:100px;width:1200px;height:700px;
  background:radial-gradient(ellipse at 40% 35%,var(--photo-b),var(--photo-a) 45%,var(--photo-c) 90%)}
.page-dim{position:absolute;inset:0;background:rgba(10,10,10,0.45)}
.page-title{position:absolute;right:28px;top:194px;font-size:34px;letter-spacing:7px;color:var(--ghost-text)}
.side-menu{position:absolute;top:364px;font-size:17px;letter-spacing:4px;color:var(--ghost-text)}
.side-menu .item-feedback{position:absolute;left:102px;top:0;white-space:nowrap}
.side-menu .item-estimate{position:absolute;left:77px;top:76px;white-space:nowrap}
.side-band{position:absolute;left:62px;top:400px;width:300px;height:26px;background:rgba(255,255,255,0.06)}
.services-panel{position:absolute;left:880px;top:350px;width:320px;height:450px;background:rgba(0,0,0,0.35)}
.services{position:absolute;right:30px;top:398px;text-align:right;color:var(--ghost-text);font-size:11px;line-height:14.5px;width:260px}
.services h2{font-weight:400;font-size:22px;letter-spacing:5px;margin-bottom:66px}
.services h3{font-weight:400;font-size:15px;margin:34px 0 24px}
.modal{position:absolute;left:150px;top:150px;width:901px;height:600px;background:var(--modal-bg);color:var(--ink)}
.modal-close{position:absolute;right:12px;top:9px;font-size:16px}
.modal-title{position:absolute;left:50px;top:48px;font-weight:400;font-size:33px;letter-spacing:6.4px}
.reviews{position:absolute;left:50px;top:147px;width:750px}
.review{height:200px;font-size:14px;line-height:18px}
.review p{margin-bottom:17px}
.review .name{font-size:13px;text-transform:uppercase}
.review .role{margin-bottom:16px}
.review .stars{font-size:13px;letter-spacing:2px}
.scrollbar{position:absolute;left:870px;top:140px;width:20px;height:410px;background:var(--ink);border:2px solid var(--ink)}
.scrollbar .thumb{display:block;width:16px;height:50px;background:var(--thumb)}
</style>
</head>
<body>
<header class="site-header">
  <div class="brand"><span class="brand-mark"></span>Tallis At Dwellings</div>
  <div class="social" aria-label="Social links"><span></span><span></span><span></span><span></span></div>
  <nav class="main-nav"><span>KITCHENS</span><span>BATHS</span><span>BASEMENTS</span><span>FINISHED CARPENTRY</span><span>DECKS &amp; PORCHES</span></nav>
</header>
<div class="hero-photo" role="img" aria-label="Photo of a finished kitchen with pendant lights and wood cabinets"></div>
<div class="page-dim"></div>
<div class="page-title">FINISHED CARPENTRY</div>
<div class="side-band"></div>
<div class="side-menu"><span class="item-feedback">CLIENTS FEEDBACK</span><span class="item-estimate">REQUEST AN ESTIMATE</span></div>
<div class="services-panel"></div>
<div class="services">
  <h2>MY SERVICES</h2>
  3D CAD MODELING OF NEW SPACES<br>CUSTOM<br>CARPENTRY &amp; FINISHES,<br><br>KITCHENS,<br>BATHS,<br>BASEMENTS,<br>DECKS,<br>PORCHES,
  <h3>WHOLE HOME RENOVATION</h3>
  SKILLED CRAFTSMANSHIP<br>(HARDWOOD FLOORING, FLOOR AND WALL TILE)<br><br>AND MUCH MORE
</div>
<section class="modal" aria-label="Client feedback">
  <div class="modal-close">CLOSE</div>
  <h1 class="modal-title">CLIENT FEEDBACK</h1>
  <div class="reviews">
    <article class="review">
      <p>Lorem ipsum dolor sit amet, consectetur adipiscing elit. Fusce sit amet ultricies magna. Cras porttitor a risus vitae congue. Aliquam porta dictum turpis in lobortis. Interdum et malesuada fames ac ante ipsum primis in faucibus.</p>
      <div class="name">John Doe</div>
      <div class="role">Entrepreneur</div>
      <div class="stars">★★★★★</div>
    </article>
    <article class="review">
      <p>Lorem ipsum dolor sit amet, consectetur adipiscing elit. Fusce sit amet ultricies magna. Cras porttitor a risus vitae congue. Aliquam porta dictum turpis in lobortis. Interdum et malesuada fames ac ante ipsum primis in faucibus.</p>
      <div class="name">John Doe</div>
      <div class="role">Entrepreneur</div>
      <div class="stars">★★★★★</div>
    </article>
  </div>
  <div class="scrollbar"><span class="thumb"></span></div>
</section>
</body>
</html>
```